Packaging Design Project for Coffee Products

Mirelle Cup is a new start-up specialising in Kopi Luwak (dubbed the most expensive coffee in the world). Due to the nature of our product, we would like to provide the premium experience and the first impression often begins with the packaging.

Our target audience is HNWs (high net-worth individuals), coffee connoisseurs, premium restaurants, cafes, and hotels. They are price insensitive and place high importance on quality and service.

We seek to have the packaging design and graphics that is artistic, clean, simple but sophisticated – representing our luxury product and premium service.

We have already thought about the packaging designs but need help when it comes to graphics and placements of information etc. Basically the packaging will consist of inner (aluminium vacuum sealed coffee pouch) and outer (paper tube) packagings.

For our detailed design specification and our logo (in EPS), please download attached files.
Updates

A number of you asked what type of font is used in the logo. The name is Philosopher. 

Project Deadline Extended
Reason: We are extending deadline by a week because we are close but not there yet. Hopefully this time extension will allow designers to tweak further their designs and submit new designs. Thanks for your understanding and cooperation. Regards MirelleCup.

Target Market(s)

HNWs (high net-worth individuals), coffee connoisseurs, premium restaurants, cafes, and hotels. They are price insensitive and place high importance o

Industry/Entity Type

Product

Requirements
Must have
• -design must be scalable as we are not yet 100% fixed on dimensions, we have provided initial reference
-please refer to our design brief for details
Should not have
• -colourful splashes
-extremely big fonts and complicated designs
-

```html
<!DOCTYPE html>
<html lang="en">
<head>
<meta charset="utf-8">
<title>MirelleCup – Kopi Luwak Tube Wrap</title>
<link rel="stylesheet" href="https://fonts.googleapis.com/css2?family=Philosopher:wght@400;700&display=swap">
<style>
  :root {
    --cap-dark: #1c0a07;
    --body-brown: #3c2317;
    --fold-line: #24120b;
    --gold: #c9a27c;
    --gold-soft: #b8916a;
    --seal-tone: #352014;
    --civet-tone: #7a5a40;
    --bean-tone: #7c4e28;
    --leaf-tone: #3d5a26;
  }
  html, body {
    margin: 0;
    padding: 0;
    width: 1178px;
    height: 1200px;
    overflow: hidden;
    background: var(--body-brown);
  }
  .wrap {
    position: relative;
    width: 1178px;
    height: 1200px;
    background: var(--body-brown);
    font-family: "Philosopher", sans-serif;
    color: var(--gold);
  }
  .cap-band {
    position: absolute;
    left: 0; top: 0;
    width: 1178px; height: 322px;
    background: var(--cap-dark);
  }
  .fold {
    position: absolute;
    top: 0;
    width: 1px;
    height: 1200px;
    background: var(--fold-line);
    z-index: 2;
  }
  .fold--a { left: 362px; }
  .fold--b { left: 590px; }
  .fold--c { left: 953px; }

  /* back panel */
  .back-panel {
    position: absolute;
    left: 0; top: 0;
    width: 376px;
    height: 1200px;
    text-align: center;
  }
  .civet-art {
    position: absolute;
    left: 98px; top: 380px;
    width: 193px; height: 126px;
    border-radius: 8px;
    background: linear-gradient(180deg, #6f5139 0%, var(--civet-tone) 100%);
  }
  .story {
    position: absolute;
    left: 0;
    width: 376px;
    margin: 0;
    font-size: 11.3px;
    line-height: 15.4px;
    color: var(--gold);
  }
  .story--1 { top: 513px; }
  .story--2 { top: 626px; }
  .story--3 { top: 826px; }
  .story--4 { top: 934px; }
  .bean-art {
    position: absolute;
    left: 162px; top: 736px;
    width: 62px; height: 66px;
    border-radius: 50%;
    background: linear-gradient(160deg, #94602f 0%, var(--bean-tone) 100%);
    transform: rotate(-25deg);
  }
  .web {
    position: absolute;
    left: 0; top: 1037px;
    width: 376px;
    font-size: 16px;
    letter-spacing: 0.3px;
  }
  .marks {
    position: absolute;
    left: 133px; top: 1064px;
    display: flex;
    align-items: center;
    gap: 8px;
  }
  .mark-circle {
    width: 24px; height: 24px;
    border-radius: 50%;
    background: var(--gold-soft);
  }
  .mark-box {
    width: 76px; height: 18px;
    border: 1px solid var(--gold-soft);
    background: rgba(201,162,124,0.18);
  }
  .address {
    position: absolute;
    left: 0; top: 1096px;
    width: 376px;
    font-size: 15px;
    line-height: 20px;
  }

  /* front panel */
  .front-panel {
    position: absolute;
    left: 590px; top: 0;
    width: 363px;
    height: 1200px;
    text-align: center;
  }
  .seal-art {
    position: absolute;
    left: 92px; top: 494px;
    width: 404px; height: 404px;
    border-radius: 50%;
    background: var(--seal-tone);
    z-index: 1;
  }
  .brand-name {
    position: absolute;
    left: 0; top: 500px;
    width: 363px;
    font-size: 42px;
    font-weight: 400;
    color: var(--gold);
    letter-spacing: 0.5px;
    z-index: 3;
  }
  .branch-art {
    position: absolute;
    left: 75px; top: 794px;
    width: 186px; height: 207px;
    border-radius: 10px;
    background: linear-gradient(200deg, var(--leaf-tone) 0%, #4a3a22 100%);
    z-index: 3;
  }
  .tagline {
    position: absolute;
    left: 0; top: 1009px;
    width: 363px;
    line-height: 1;
  }
  .tagline__small { display: block; font-size: 18.5px; }
  .tagline__main { display: block; font-size: 24px; margin: 8px 0 6px; letter-spacing: 0.4px; }
  .net-weight {
    position: absolute;
    left: 0; top: 1135px;
    width: 363px;
    font-size: 16px;
  }
</style>
</head>
<body>
<div class="wrap">
  <div class="cap-band"></div>
  <div class="fold fold--a"></div>
  <div class="fold fold--b"></div>
  <div class="fold fold--c"></div>

  <section class="back-panel">
    <div class="civet-art" role="img" aria-label="Engraved-style illustration of a walking Asian civet"></div>
    <p class="story story--1">From the archipelago of Indonesia, MirelleCup brings you<br>the finest exotic coffee on the planet – Kopi Luwak. Of<br>course, we can't do this alone – thanks to Luwak (Asian<br>Civet) who eat only the ripest and reddest coffee cherries,<br>process them through their digestive systems and produce<br>the unique taste through enzyme fermentation.</p>
    <p class="story story--2">We carefully clean and select individual beans. We then<br>roast them to perfection (light to medium roast) to bring<br>out their full-bodied distinct flavours, their rich aroma as<br>well as their smooth and clean lingering aftertaste.<br>We want to share with you what we cherish, revere and<br>venerate - the premium gourmet coffee experience!</p>
    <div class="bean-art" role="img" aria-label="Photograph of a single roasted coffee bean"></div>
    <p class="story story--3">From the archipelago of Indonesia, MirelleCup brings you<br>the finest exotic coffee on the planet – Kopi Luwak. Of<br>course, we can't do this alone – thanks to Luwak (Asian<br>Civet) who eat only the ripest and reddest coffee cherries,<br>process them through their digestive systems and produce<br>the unique taste through enzyme fermentation.</p>
    <p class="story story--4">We carefully clean and select individual beans. We then<br>roast them to perfection (light to medium roast) to bring<br>out their full-bodied distinct flavours, their rich aroma as<br>well as their smooth and clean lingering aftertaste.<br>We want to share with you what we cherish, revere and<br>venerate - the premium gourmet coffee experience!</p>
    <div class="web">www.mirellecup.com</div>
    <div class="marks">
      <span class="mark-circle"></span>
      <span class="mark-box"></span>
    </div>
    <div class="address">MirelleCup<br>Larkspur 40517<br>Indonesia</div>
  </section>

  <section class="front-panel">
    <div class="seal-art" role="img" aria-label="Faint round authenticity stamp for pure Kopi Luwak"></div>
    <div class="brand-name">MirelleCup</div>
    <div class="branch-art" role="img" aria-label="Illustration of a coffee branch with green leaves and ripe red cherries"></div>
    <div class="tagline">
      <span class="tagline__small">premium exotic</span>
      <span class="tagline__main">GOURMET COFFEE</span>
      <span class="tagline__small">experience</span>
    </div>
    <div class="net-weight">Net Weight 200gr</div>
  </section>
</div>
</body>
</html>
```